Flyer Advertising Summer Programs for students - 6x9 inches

We need a 6x9 front and back flyer to advertise our summer programs. We are an interfaith organization that does programs with youth of all religious and non-religious backgrounds. I've sent our logos, copy, pictures, etc. that you can work with to make it pop!

Target Market(s)

youth and their parents and religious communities

Industry/Entity Type

Non Profit

Font styles to use
Serif

Requirements
Must have
• The project needs to have a place for a mailing label and stamp and our return address. It should also include lots of pictures, our logos, be fun, and eye-catching.
Nice to have
• pictures, logo, etc.

```html
<!DOCTYPE html>
<html lang="en">
<head>
<meta charset="utf-8">
<title>Summer Programs Flyer – Back</title>
<link href="https://fonts.googleapis.com/css2?family=Source+Sans+3:ital,wght@0,400;0,600;0,700;1,400;1,700&display=swap" rel="stylesheet">
<style>
  :root {
    --orange: #f26522;
    --ink: #2a2a2a;
    --white: #ffffff;
    --paper: #fbf7f3;
    --line: #9a9a9a;
    --photo-top-a: #8fa3b8;
    --photo-top-b: #5c6e63;
    --photo-inset-a: #d9d4c8;
    --photo-inset-b: #6e6a60;
  }
  * { box-sizing: border-box; margin: 0; padding: 0; }
  html, body { width: 802px; height: 1200px; overflow: hidden; background: var(--paper); }
  body { font-family: "Source Sans 3", Arial, sans-serif; color: var(--ink); }
  .flyer { position: relative; width: 802px; height: 1200px; background: var(--paper); overflow: hidden; }
  .nowrap { white-space: nowrap; }

  .hero-photo {
    position: absolute; left: 0; top: 0; width: 802px; height: 348px;
    background: linear-gradient(180deg, var(--photo-top-a) 0%, #a9b6bf 45%, var(--photo-top-b) 100%);
  }
  .trip-box {
    position: absolute; left: 0; top: 0; width: 282px; height: 348px;
    background: var(--white); padding: 12px 16px 0 16px;
  }
  .trip-title { font-weight: 700; font-size: 25px; line-height: 1.1; color: var(--ink); }
  .trip-text { font-size: 21px; line-height: 1.2; color: var(--ink); margin-top: 4px; text-align: justify; }
  .trip-register { font-weight: 700; font-size: 21px; line-height: 1.2; color: var(--orange); }

  .program-band {
    position: absolute; left: 0; top: 348px; width: 802px; height: 322px;
    background: var(--orange); padding: 30px 60px 0 60px;
  }
  .program-intro { color: var(--white); font-size: 24px; line-height: 1.35; text-align: justify; text-align-last: center; }
  .program-list { list-style: none; margin-top: 14px; padding-left: 190px; }
  .program-list li { font-weight: 700; font-size: 24px; line-height: 1.45; color: var(--ink); }

  .group-photo {
    position: absolute; left: 40px; top: 682px; width: 296px; height: 350px;
    border: 8px solid var(--white); box-shadow: 0 2px 6px rgba(0,0,0,.25);
    background: linear-gradient(180deg, var(--photo-inset-a) 0%, #bdb6a8 50%, var(--photo-inset-b) 100%);
  }
  .stamp-box {
    position: absolute; left: 614px; top: 766px; width: 122px; height: 126px;
    border: 2px solid var(--line); background: var(--white);
  }
  .address-lines { position: absolute; left: 410px; top: 926px; width: 326px; }
  .address-lines span { display: block; height: 2px; background: var(--line); margin-bottom: 34px; }

  .return-address {
    position: absolute; left: 0; top: 1042px; width: 802px;
    font-style: normal; font-size: 14px; line-height: 20px; color: var(--ink);
  }
  .return-address .row { display: flex; justify-content: center; align-items: center; gap: 6px; height: 20px; }
  .return-address .dot { width: 11px; height: 11px; background: var(--orange); border-radius: 50%; display: inline-block; }
  .return-address .sq { width: 11px; height: 11px; background: var(--orange); display: inline-block; }
  .return-address svg { width: 12px; height: 14px; }

  .site-bar {
    position: absolute; left: 0; top: 1152px; width: 802px; height: 48px;
    background: var(--orange); color: var(--white); text-align: center;
    font-weight: 600; font-size: 22px; letter-spacing: 5px; line-height: 48px;
  }
</style>
</head>
<body>
<main class="flyer">
  <div class="hero-photo" role="img" aria-label="Group of students standing on the Capitol steps in Washington DC"></div>

  <section class="trip-box">
    <h2 class="trip-title">Washington DC Trip</h2>
    <p class="trip-text">June 11-16 – join hundreds of other students to visit lawmakers and advocacy groups through the Capitol Forward Program! Cost: $600.</p>
    <p class="trip-register">To register, visit <span class="nowrap">www.yfli-summer.org</span></p>
  </section>

  <section class="program-band">
    <p class="program-intro">Youth Faith Leaders Initiative join students from all over Los Angeles and Orange Counties for community service, leadership development, visiting various places of worship, and fun! You can earn a $100 college scholarship! To sign up, visit <span class="nowrap">www.yfli-summer.org</span></p>
    <ol class="program-list">
      <li>1.Westbridge University July 18-20</li>
      <li>2.Orangewood College July 25-27</li>
      <li>3.Harborview State August 1-3</li>
    </ol>
  </section>

  <div class="group-photo" role="img" aria-label="Students posing together in front of a large stone memorial statue"></div>

  <div class="stamp-box" aria-label="Stamp area"></div>
  <div class="address-lines" aria-label="Mailing label area"><span></span><span></span><span></span></div>

  <address class="return-address">
    <div class="row">
      <svg viewBox="0 0 12 14" aria-hidden="true"><path d="M6 0C2.7 0 0 2.6 0 5.8 0 10 6 14 6 14s6-4 6-8.2C12 2.6 9.3 0 6 0zm0 8a2.2 2.2 0 1 1 0-4.4A2.2 2.2 0 0 1 6 8z" fill="#f26522"/></svg>
      <span>418 Maple Crest Avenue, Alderton, CA 90000</span>
    </div>
    <div class="row"><i class="sq"></i><span>Common Ground Partners and Youth Faith Leaders Initiative</span></div>
    <div class="row">
      <i class="dot"></i><span>@CGPnews</span>
      <i class="dot"></i><span>CommonGroundYouth</span>
      <i class="sq"></i><span>hello@commongroundpartners.org</span>
    </div>
  </address>

  <footer class="site-bar">www.commongroundpartners.org</footer>
</main>
</body>
</html>
```